Young, modern, highly skilled carpenter needs business card design

I need a business card design for my construction business. Its called 'Pemberton Building Partners'. Im looking for a ultra modern design that incorporates P B P, the first letters of the name with only a subtle reference to carpentry. The design should reflect my high quality work and eye for detail. i have also uploaded some exmaple designs i like.

Industry/Entity Type

Construction

Requirements
Must have
• Name of business, my name, mobile number, ABN number, email address
Nice to have
• A logo incorporating the name of the business

```html
<!DOCTYPE html>
<html lang="en">
<head>
<meta charset="utf-8">
<title>Pemberton Building Partners – Business Card</title>
<link rel="stylesheet" href="https://fonts.googleapis.com/css2?family=Open+Sans:wght@400;600;700&display=swap">
<style>
  :root {
    --page-bg: #ffffff;
    --ink: #000000;
    --navy-deep: #1c1f4a;
    --navy-mid: #2b3a66;
    --grey-text: #8a8a8a;
    --grey-mark: #9a9a9a;
    --card-border: #555555;
    --white: #ffffff;
  }
  * { box-sizing: border-box; margin: 0; padding: 0; }
  html, body {
    width: 1200px;
    height: 645px;
    overflow: hidden;
    background: var(--page-bg);
    font-family: "Open Sans", Arial, sans-serif;
    color: var(--ink);
  }
  .sheet { position: relative; width: 1200px; height: 645px; }

  .side-label {
    position: absolute;
    font-size: 18px;
    font-weight: 400;
    transform: translateX(-50%);
  }
  .side-label--front { left: 425px; top: 180px; }
  .side-label--back { left: 913px; top: 72px; }

  /* Front */
  .card-front {
    position: absolute;
    left: 180px; top: 269px;
    width: 458px; height: 265px;
    overflow: hidden;
  }
  .card-front__pattern {
    position: absolute; inset: 0;
    background: radial-gradient(circle at 55% 40%, var(--navy-mid) 0%, var(--navy-deep) 75%);
  }
  .card-front__mark {
    position: absolute;
    left: 16px; bottom: 18px;
    display: flex; align-items: center; gap: 8px;
    color: var(--white);
    font-size: 40px;
    font-weight: 400;
    letter-spacing: 2px;
    line-height: 1;
  }
  .mark-square {
    width: 10px; height: 10px;
    background: var(--white);
  }

  /* Back */
  .card-back {
    position: absolute;
    left: 789px; top: 115px;
    width: 264px; height: 467px;
    border: 1.5px solid var(--card-border);
    background: var(--white);
    text-align: center;
  }
  .card-back__mark {
    position: absolute;
    left: 0; right: 0; top: 72px;
    display: flex; justify-content: center; align-items: center; gap: 8px;
    color: var(--grey-mark);
    font-size: 40px;
    font-weight: 400;
    letter-spacing: 2px;
    line-height: 1;
  }
  .card-back__mark .mark-square { background: var(--grey-mark); }

  .holder-name {
    position: absolute; left: 0; right: 0; top: 190px;
    font-size: 28px; font-weight: 700; line-height: 1.1;
  }
  .holder-role {
    position: absolute; left: 0; right: 0; top: 226px;
    font-size: 13px; font-weight: 700;
  }
  .company {
    position: absolute; left: 0; right: 0; top: 290px;
    color: var(--grey-text);
  }
  .company__name { font-size: 15px; font-weight: 700; line-height: 1.2; }
  .company__abn { font-size: 12px; font-weight: 700; }
  .contact {
    position: absolute; left: 0; right: 0; top: 345px;
    color: var(--grey-text);
    font-size: 15px; line-height: 1.25;
    list-style: none;
  }
  .location {
    position: absolute; left: 0; right: 0; top: 416px;
    color: var(--grey-text);
    font-size: 15px; font-weight: 700;
  }
</style>
</head>
<body>
<main class="sheet">
  <p class="side-label side-label--front">Front</p>
  <p class="side-label side-label--back">Back</p>

  <section class="card-front" aria-label="Business card front">
    <div class="card-front__pattern" role="img" aria-label="Navy background with a repeating interlocking ring pattern"></div>
    <div class="card-front__mark"><span>PBP</span><span class="mark-square"></span></div>
  </section>

  <section class="card-back" aria-label="Business card back">
    <div class="card-back__mark"><span>PBP</span><span class="mark-square"></span></div>
    <h1 class="holder-name">Sam R. Carter</h1>
    <p class="holder-role">master carpenter</p>
    <div class="company">
      <p class="company__name">Pemberton Building Partners</p>
      <p class="company__abn">ABN- 518203746921</p>
    </div>
    <ul class="contact">
      <li>+1.555.204.7731</li>
      <li>sam@pbpbuild.com</li>
      <li>pbpbuild.com</li>
    </ul>
    <p class="location">New York City</p>
  </section>
</main>
</body>
</html>
```